Brennick Setter Club - Rare dog breed club needs web design!

The Transylvanian Hound (or Erdélyi kopó) is an ancient Hungarian dog breed. These medium-sized hounds were favored by the Hungarian kings and princes for hunting bears and wolves in the Carpathian mountains of Transylvania. The breed's great adaptability to the region's extreme climates of sweltering summers and frigid winters made it an excellent all season hunting dog. This dog has a sleek appearance and stunning good looks. They are lean, appear very elegant and proud. Their erect posture and beautifully sculpted head portray great attentiveness and authority. In general, this rare breed is extremely good natured, loyal and obedient. It has a tendency to form strong attachments to its primary caretakers and will remain loyal and protective. (Please refer to existing web resources.)

The Brennick Setter Club - with current website www.brennicksetter.com - is the official breed club of Transylvanian Hound afficionados, breeders and owners in the United States, which was founded in 2010. We are looking for a web design for the new, upgraded version of this central (currenty non-functioning) website. Please do not recycle the old logo (we may choose from your suggesions and pay for it!) or any of the old texts. Please use the structure described below. Overall, the webpage serves a dual purpose: an educational one (about the breed itself) and a community-building one (inside the Club). The proposed structure of the website is as follows:

1. About the Kopó
- Breed History
- Breed Standard
- Public Education
- Photo Gallery

2. Life with a Kopó
- Health and Genetics
- Feeding and Nutrition
- Training and Activities

3. Finding a Kopó
- Is this the Right Breed for You?
- Choosing a Puppy
- FAQ
- Breeder Referral

4. The Brennick Setter Club
- Constituton
- Officers and Appointees
- Code of Ethics
- Breeder Guidelines
- Membership
- Reports
- Links

5. News and Events

6. Shop

We are attaching a couple of examples of the graphics/drawings of the dogs that would be part of the design of the website. We plan to have more of these artistic depictions, nicely embedded into the background (maybe shaded out at the edges just like the drawings themselves) and less actual photos. Or a good combination of the two.

Further information upon request.

Reason: There are a few very promising design collaborations ongoing. As we moved the brief to a more artistic and graphic direction, we felt that one week of extension would be needed to get to the perfect end-product, which could include designs for sub-pages as well.

Reason: In order to make the final modifications to the leading designs, and at the request of those designers, the deadline is extended until Friday.

Target Market(s)

- BRSC Club members, dog (especially T-Hound) owners, past and future owners, breeders, puppy buyers, hunters, kennel clubs, dog show participants, vets, animal shelters, Hungarian, Romanian and other European web visitors, historians

Industry/Entity Type

Club

Font styles to use
Serif
Decorative
Script

Requirements
Must have
• - Sync with graphics of dogs (see attachments), but accentuate the rich black basic color of the dogs
- Elegance, aristocratic/noble look and feel (but not overly archaic)
- Love, companionship, dogs as family members
- Hunting usage, but no bloody associations, rather romantic ones
- Simple to use and navigate for non-web-natives
- Old world (Central European) atmosphere, even the exotic, rustic and romantic Transylvanian feel - SEE the new attachment for inspiration (this was a design plan which we discarded (mainly because of its gothic, (nazi-like), unreadable font, and the fact that the plan makes the black-looking dogs appear brown), however we loved the fact that it was not full of boxes/windows, had a marble/sand stone like continuous background, lots of little elegant graphics, the drawings embedded, etc.
Nice to have
• - Working on smartphone, Zentabs, etc., so dynamic website design
- Web shop to be added to functionalities in the future (?)
- English language for now, in the future can be Hungarian, Romanian, etc., so the font choice should handle various alphabets
- Focus on the dogs (likely more graphics than photos, at least on the main pages), and not on the activities/humans - the design should accentuate the black and not the tan of the graphics!
Should not have
• - Old logo from the old www.brennicksetter.com webpage or the other logo from the Chatterly site of the Brennick Setter Club, we will have a new one (maybe designed by you!)
- Breed club, kennel club cliches
- Cutesy, adorable, cheesy design elements
- Old, stale, monolithic, archaic, snobbish, etc. look and feel
- No vampire associations

```html
<!DOCTYPE html>
<html lang="en">
<head>
<meta charset="utf-8">
<title>Brennick Setter Club</title>
<link href="https://fonts.googleapis.com/css2?family=Roboto:ital,wght@0,300;0,400;0,500;1,400&display=swap" rel="stylesheet">
<style>
:root{
  --sand:#efe4cf;
  --sand-dark:#e2d3b6;
  --panel:#f7f3ec;
  --ink:#1f1a18;
  --text:#4a4440;
  --nav-dark:#231b18;
  --card:#f6ead0;
  --card-line:#e6d6b2;
  --button:#4a4544;
  --footer:#2b201c;
  --footer-text:#cbbfb4;
  --frame:#ffffff;
}
*{box-sizing:border-box;margin:0;padding:0}
html,body{width:1028px;height:1200px;overflow:hidden}
body{
  position:relative;
  font-family:"Roboto",Arial,sans-serif;
  color:var(--text);
  background:linear-gradient(180deg,var(--sand) 0%,#f1e8d6 60%,var(--sand-dark) 100%);
}
.sketch{position:absolute;border-radius:50%;filter:blur(6px)}
.sketch-left{left:-40px;top:160px;width:150px;height:360px;background:radial-gradient(ellipse at center,rgba(90,70,55,.35),rgba(90,70,55,0) 70%)}
.sketch-right{left:810px;top:-10px;width:230px;height:200px;background:radial-gradient(ellipse at center,rgba(70,55,45,.3),rgba(70,55,45,0) 70%)}

.panel{position:absolute;left:84px;top:49px;width:859px;height:1030px;background:var(--panel);box-shadow:0 0 6px rgba(0,0,0,.15)}

.logo{position:absolute;left:94px;top:13px;width:132px;height:132px;border-radius:50%;background:#fff;border:3px solid var(--ink);display:flex;align-items:center;justify-content:center;text-align:center;z-index:3}
.logo span{font-size:15px;font-weight:500;color:var(--ink);line-height:1.2;letter-spacing:.5px;text-transform:uppercase;width:96px}

.follow{position:absolute;left:788px;top:15px;display:flex;align-items:center;gap:6px;font-size:11px;color:var(--ink)}
.follow .net{display:flex;align-items:center;gap:3px;font-size:10px;color:var(--ink)}
.follow .net i{width:8px;height:8px;border-radius:50%;background:var(--button);display:block}

.nav{position:absolute;left:274px;top:66px;display:flex;font-size:11px;text-transform:uppercase;color:var(--ink);z-index:2}
.nav li{list-style:none;padding:0 8.5px;height:46px;line-height:46px;position:relative}
.nav li.active{background:var(--nav-dark);color:#fff;padding:0 10px 0 12px}
.dropdown{position:absolute;left:0;top:46px;width:136px;background:var(--nav-dark);padding:4px 0 6px 12px;text-transform:none}
.dropdown a{display:block;font-size:10px;font-style:italic;color:#e8dfd6;line-height:21.3px;text-decoration:none}
.dropdown a::before{content:"→";font-style:normal;font-size:8px;margin-right:8px}

.hero{position:absolute;left:95px;top:113px;width:838px;height:326px;background:var(--frame);border:1px solid #ddd2c2;padding:4px}
.hero .photo{width:100%;height:100%;background:linear-gradient(180deg,#5a3a22 0%,#7a4a25 45%,#a35a25 80%,#8a4a22 100%)}
.dots{position:absolute;left:395px;top:304px;display:flex;gap:5px}
.dots span{width:11px;height:11px;border-radius:50%;background:#fff}
.dots span.on{background:transparent;border:1.5px solid #fff}

.welcome{position:absolute;left:84px;width:859px;top:464px;text-align:center;font-size:17px;font-weight:400;color:var(--ink)}
.strip{position:absolute;left:95px;top:503px;width:838px;height:113px;display:flex;gap:1px}
.strip div{flex:1}
.strip .p1{background:linear-gradient(135deg,#8fb9e0,#3a3230)}
.strip .p2{background:linear-gradient(180deg,#6a6a58,#7a7a48)}
.strip .p3{background:linear-gradient(180deg,#8a8478,#5a4a40)}
.strip .p4{background:linear-gradient(135deg,#2f4a1e,#5a3a22)}

.intro{position:absolute;left:150px;top:632px;width:728px;text-align:center;font-size:9.6px;line-height:17px;font-weight:300;color:var(--text)}
.rule{position:absolute;left:95px;top:706px;width:838px;height:1px;background:#d8cebf}

.card{position:absolute;top:728px;width:263px;height:328px;background:var(--card);border:1px solid var(--card-line);text-align:center}
.card h2{font-size:17px;font-weight:400;color:var(--ink);margin-top:16px;height:24px}
.card .photo{margin:6px auto 0;width:233px;height:118px}
.card p{font-size:9.6px;line-height:17px;font-weight:300;color:var(--text);padding:11px 15px 0}
.card .btn{position:absolute;left:86px;top:287px;width:90px;height:29px;line-height:29px;background:var(--button);color:#fff;font-size:10px;text-transform:uppercase;border-radius:2px}
.c1{left:95px}.c2{left:382px}.c3{left:669px}
.c1 .photo{background:linear-gradient(180deg,#7a8a8a,#5a7a3a)}
.c2 .photo{background:linear-gradient(180deg,#4a6a2a,#2a4a1a)}
.c3 .photo{background:linear-gradient(90deg,#d8d8d8 0%,#6a6a6a 20%,#2a2a2a 60%,#9a9a9a 100%)}

.footer{position:absolute;left:0;top:1079px;width:1028px;height:121px;background:var(--footer)}
.footer nav{position:absolute;left:95px;top:29px;display:flex;gap:15px;font-size:10px;color:var(--footer-text)}
.copy{position:absolute;left:95px;top:70px;font-size:9px;line-height:16px;color:var(--footer-text)}
.copy b{color:#fff;font-weight:400}
.badge{position:absolute;top:33px;width:56px;height:56px;border-radius:50%;background:#dcdcdc;border:2px solid #fff}
.b1{left:805px;background:#b9c4d4}.b2{left:875px}
</style>
</head>
<body>
<div class="sketch sketch-left" role="img" aria-label="Faded pencil drawing of hound heads"></div>
<div class="sketch sketch-right" role="img" aria-label="Faded pencil drawing of a hound"></div>

<div class="panel"></div>

<div class="logo"><span>Brennick Setter Club</span></div>

<div class="follow">Follow Us:
  <span class="net"><i></i>Chatterly</span>
  <span class="net"><i></i>Flitter</span>
  <span class="net"><i></i>Reelbox</span>
</div>

<ul class="nav">
  <li class="active">About the Kopó
    <div class="dropdown">
      <a>Breed History</a><a>Breed Standard</a><a>Public Education</a><a>Photo Gallery</a>
    </div>
  </li>
  <li>Life with a Kopó</li>
  <li>Finding a Kopó</li>
  <li>The Brennick Setter Club</li>
  <li>News and Events</li>
  <li>Shop</li>
</ul>

<div class="hero">
  <div class="photo" role="img" aria-label="Three black and tan hounds sitting in autumn leaves"></div>
  <div class="dots"><span class="on"></span><span></span><span></span><span></span></div>
</div>

<h1 class="welcome">Welcome to Brennick Setter Club</h1>

<div class="strip">
  <div class="p1" role="img" aria-label="Puppy lying on a blue blanket"></div>
  <div class="p2" role="img" aria-label="Group of hounds standing on grass"></div>
  <div class="p3" role="img" aria-label="Hounds resting on a patio"></div>
  <div class="p4" role="img" aria-label="Portrait of a hound outdoors"></div>
</div>

<p class="intro">Aliquam molestie, mi et imperdiet euismod, dui purus auctor tellus, et interdum lacus lectus et ante. Sed accumsan sollicitudin sapien, sit amet adipiscing turpis gravida ac. In congue, neque ac lobortis volutpat, libero mauris varius mi, vitae suscipit ipsum ligula vitae risus. Duis aliquam nibh a dui iaculis viverra id a velit. Vivamus egestas risus in magna varius commodo. Sed semper viverra egestas. Etiam pretium porttitor lectus, vel ornare neque porta volutpat.</p>
<div class="rule"></div>

<div class="card c1">
  <h2>The Brennick Setter Club</h2>
  <div class="photo" role="img" aria-label="Club member walking hounds in a garden"></div>
  <p>Aliquam molestie, mi et imperdiet euismod, dui purus auctor tellus, et interdum lacus lectus et ante. Sed accumsan sollicitudin sapien, sit amet adipiscing turpis gravida ac. In congue, neque ac lobortis volutpat, libero mauris varius mi, vitae suscipit ipsum ligula vitae risus.</p>
  <div class="btn">Read More</div>
</div>
<div class="card c2">
  <h2>Life with a Kopó</h2>
  <div class="photo" role="img" aria-label="Hounds playing in tall grass"></div>
  <p>Aliquam molestie, mi et imperdiet euismod, dui purus auctor tellus, et interdum lacus lectus et ante. Sed accumsan sollicitudin sapien, sit amet adipiscing turpis gravida ac. In congue, neque ac lobortis volutpat, libero mauris varius mi, vitae suscipit ipsum ligula vitae risus.</p>
  <div class="btn">Read More</div>
</div>
<div class="card c3">
  <h2>Finding a Kopó</h2>
  <div class="photo" role="img" aria-label="Young hound by a porch"></div>
  <p>Aliquam molestie, mi et imperdiet euismod, dui purus auctor tellus, et interdum lacus lectus et ante. Sed accumsan sollicitudin sapien, sit amet adipiscing turpis gravida ac. In congue, neque ac lobortis volutpat, libero mauris varius mi, vitae suscipit ipsum ligula vitae risus.</p>
  <div class="btn">Read More</div>
</div>

<footer class="footer">
  <nav>
    <span>About the Kopó</span><span>Life with a Kopó</span><span>Finding a Kopó</span><span>The Brennick Setter Club</span><span>News and Events</span><span>Shop</span>
  </nav>
  <div class="copy">Copyright © 2014. <b>Brennick Setter Club</b> .<br>All Right Reserved</div>
  <div class="badge b1"></div>
  <div class="badge b2"></div>
</footer>
</body>
</html>
```